home accents e-commerce website

I'd like a professional simple website designed where I can sell my home goods. I already have my domain name registered. I need the website to accept credit card payments and Tendrix. It should have a shopping cart option and calculate sales tax and shipping costs on merchandise automatically.

I'll be taking photographs of the merchandise and writing product descriptions myself. (I'm not a professional photographer, so these photos probably won't look too polished. If you can help me make them look better, that'd be great). As I add new merchandise in the future, I'd like an option where I can log in to the back end myself and add pictures/product descriptions. And take old products down as they sell out. So the website needs to be user-friendly for me, even though I'm completely web design illiterate!

I'd like a creative, talented person who can create a whimsical, cute website. Nothing too corporate-looking.

Thank you!

Target Market(s)

women, online shoppers, New York City-area, (ship products to the United States only)

Industry/Entity Type

Home And Garden

Coding

Coded - Design and coding required

Number of Pages Required

1 page

Font styles to use
Sans Serif

Colors
0355a3
ffffff

Requirements
Must have
• shopping cart feature
• safe, secure credit card and Tendrix payments
• ability for me to go in and add new products and take down old/sold products
Nice to have
• whimsical, cute design
Should not have
• too corporate-looking

```html
<!DOCTYPE html>
<html lang="en">
<head>
<meta charset="utf-8">
<title>Nestory Home Goods</title>
<link href="https://fonts.googleapis.com/css2?family=Mulish:wght@300;400;600;700&display=swap" rel="stylesheet">
<style>
:root{
  --brand:#0355a3;
  --brand-dark:#0a4380;
  --brand-light:#1f6bbd;
  --white:#ffffff;
  --ink:#333a44;
  --muted:#8a8f96;
  --price-bg:#dde6f1;
  --line:#d9dde2;
  --band:#ececec;
}
*{box-sizing:border-box;margin:0;padding:0}
html,body{width:1200px;height:2507px;overflow:hidden;background:var(--white)}
body{position:relative;font-family:"Mulish",Arial,sans-serif;color:var(--ink)}
a{color:inherit;text-decoration:none}
.abs{position:absolute}

/* top bar */
.topbar{left:0;top:0;width:1200px;height:44px;background:var(--brand)}
.topbar .social{left:795px;top:9px;display:flex;gap:7px}
.topbar .social span{width:25px;height:25px;border:1.5px solid var(--white);border-radius:50%;display:block}
.cart{left:961px;top:0;width:109px;height:44px;background:var(--brand-dark);color:var(--white);font-size:12px;font-weight:600;display:flex;align-items:center;justify-content:center;gap:8px}

/* hero */
.hero{left:0;top:44px;width:1200px;height:641px;background:linear-gradient(100deg,#dfe6ea 0%,#eef0ef 30%,#f1eeea 55%,#e9e2da 80%,#dcd3ca 100%);overflow:hidden}
.hero-curve{left:0;top:44px;width:1200px;height:140px}
.nav{top:90px;font-size:19px;color:#555c66}
.logo{text-align:center;color:var(--brand)}
.logo .word{font-size:44px;font-weight:700;line-height:1;letter-spacing:1px}
.logo .sub{font-size:14px;letter-spacing:6px;margin-top:4px}
.hero-kicker{left:126px;top:296px;font-size:28px;color:var(--brand);font-weight:400}
.hero-title{left:125px;top:338px;font-size:50px;line-height:61px;font-weight:400;color:#1d232b}
.btn-hero{left:127px;top:485px;width:160px;height:47px;background:var(--brand);color:var(--white);font-size:19px;font-weight:700;display:flex;align-items:center;justify-content:center;border-radius:3px}
.hero-photo{left:585px;top:260px;width:485px;height:317px;border-radius:14px;background:linear-gradient(180deg,#6a5cc4 0%,#7e5f4a 35%,#8a7a86 60%,#8a8a3a 100%)}
.dots{left:558px;top:624px;display:flex;gap:9px}
.dots span{width:14px;height:14px;border-radius:50%;background:var(--white)}
.dots span.off{background:transparent;border:2px solid var(--white)}

/* sidebar */
.categories{left:117px;top:760px;width:249px;height:415px;background:var(--brand-dark)}
.categories h2{height:49px;background:var(--brand-light);color:var(--white);font-size:23px;font-weight:400;padding:11px 0 0 35px}
.categories ul{list-style:none;padding:22px 0 0 38px}
.categories li{color:#e6eef7;font-size:16px;height:34.7px;position:relative;padding-left:17px}
.categories li::before{content:"";position:absolute;left:0;top:6px;border-left:5px solid #cfdcec;border-top:4px solid transparent;border-bottom:4px solid transparent}
.promo{left:117px;top:1190px;width:249px;height:275px;border:1px solid var(--line);background:var(--white);box-shadow:0 1px 4px rgba(0,0,0,.12)}
.promo-photo{height:163px;background:linear-gradient(135deg,#2f3a8a 0%,#5a5fb0 45%,#d7c4b0 100%)}
.promo .kicker{font-size:17px;color:var(--brand);margin:8px 0 0 19px}
.promo .title{font-size:24px;color:var(--brand);margin:1px 0 0 19px;line-height:1.1}
.promo .click{margin:10px 0 0 22px;width:88px;height:28px;border:1.5px solid var(--brand);color:var(--brand);font-size:12px;display:flex;align-items:center;justify-content:center}

/* products */
.section-title{font-size:28px;font-weight:400;color:#222}
.card{width:216px;height:305px;border:1px solid var(--line);background:var(--white)}
.card .photo{position:absolute;left:28px;top:22px;width:158px;height:150px;border-radius:8px}
.card .name{position:absolute;left:0;right:0;top:204px;text-align:center;font-size:19px;color:#333}
.card .desc{position:absolute;left:0;right:0;top:231px;text-align:center;font-size:12px;color:var(--muted)}
.card .bar{position:absolute;left:0;right:0;bottom:0;height:37px;display:flex}
.card .price{width:50%;background:var(--price-bg);color:var(--brand);font-size:17px;display:flex;align-items:center;justify-content:center}
.card .buy{width:50%;background:var(--brand);color:var(--white);font-size:15px;font-weight:600;display:flex;align-items:center;justify-content:center}
.card.tall{width:221px;height:314px}
.card.tall .photo{left:30px;top:30px;width:161px;height:140px}
.card.tall .name{top:212px}
.card.tall .desc{top:238px}

/* top sellings */
.sellers{left:0;top:1532px;width:1200px;height:485px;background:linear-gradient(90deg,#c9d3e0 0%,#dfe3ea 30%,#ecebec 55%,#e8dfd8 80%,#d6cfd4 100%);border-top:1.5px dashed #b8c0cc;border-bottom:1.5px dashed #b8c0cc}

/* newsletter */
.newsletter{left:0;top:2017px;width:1200px;height:102px;background:var(--band)}
.newsletter h3{position:absolute;left:219px;top:33px;font-size:28px;font-weight:400;color:#222}
.newsletter .field{position:absolute;left:486px;top:33px;width:396px;height:37px;background:var(--white);border:1px solid #cfd3d8;font-size:12px;color:var(--muted);padding:11px 0 0 17px}
.newsletter .send{position:absolute;left:882px;top:33px;width:114px;height:37px;background:var(--brand);color:var(--white);font-size:16px;font-weight:600;display:flex;align-items:center;justify-content:center}

/* footer */
.foot-col h4{font-size:19px;font-weight:600;color:var(--brand);margin-bottom:16px}
.foot-col li{list-style:none;font-size:15px;color:#666;height:30px;padding-left:5px}
.foot-social{display:flex;gap:8px}
.foot-social span{width:37px;height:37px;border:2px solid var(--brand);border-radius:50%;display:block}
.pay{display:flex;gap:10px;margin-top:19px}
.pay span{width:41px;height:25px;background:#eef0f3;border:1px solid #dadde2;font-size:8px;font-weight:700;color:var(--brand);display:flex;align-items:center;justify-content:center}
.rule{left:117px;top:2433px;width:966px;height:1px;background:#cfd3d8}
.copy{left:0;width:1200px;top:2455px;text-align:center;font-size:14px;color:#777}
</style>
</head>
<body>

<header>
  <div class="abs topbar">
    <div class="abs social"><span></span><span></span><span></span><span></span></div>
    <a class="abs cart" href="#">
      <svg width="20" height="16" viewBox="0 0 20 16" fill="none" stroke="#fff" stroke-width="1.6"><path d="M1 1h3l2.5 9h10l2-6.5H5.2"/><circle cx="8" cy="13.5" r="1.4"/><circle cx="15" cy="13.5" r="1.4"/></svg>
      0 ITEMS
    </a>
  </div>
</header>

<section class="abs hero" role="img" aria-label="Blurred bright living room interior"></section>
<svg class="abs hero-curve" viewBox="0 0 1200 140" preserveAspectRatio="none">
  <path d="M0 0H1200V53C900 140 300 140 0 53Z" fill="#ffffff"/>
  <path d="M0 57C300 144 900 144 1200 57" fill="none" stroke="#c9d3de" stroke-width="2"/>
</svg>
<nav>
  <a class="abs nav" style="left:210px" href="#">About Nestory</a>
  <a class="abs nav" style="left:374px" href="#">Contact</a>
  <div class="abs logo" style="left:492px;top:68px;width:220px">
    <div class="word">Nestory</div>
    <div class="sub">HOME GOODS</div>
  </div>
  <a class="abs nav" style="left:740px" href="#">How does this craziness work?</a>
</nav>
<p class="abs hero-kicker">Special Offers</p>
<h1 class="abs hero-title">Home Goods<br>and Throw Pillows</h1>
<a class="abs btn-hero" href="#">BUY NOW</a>
<div class="abs hero-photo" role="img" aria-label="Stack of folded blankets and throws topped with a purple pillow"></div>
<div class="abs dots"><span class="off"></span><span></span><span></span><span></span></div>
<svg class="abs" style="left:0;top:640px" width="1200" height="90" viewBox="0 0 1200 90">
  <path d="M0 60C350 0 850 0 1200 55" fill="none" stroke="#e3e7ec" stroke-width="2"/>
  <path d="M0 45H1200V90H0Z" fill="#ffffff"/>
  <path d="M0 46C400 15 800 15 1200 46" fill="#ffffff"/>
</svg>

<aside>
  <div class="abs categories">
    <h2>Categories</h2>
    <ul>
      <li>Vases</li><li>Throw Pillows</li><li>Blankets and Throws</li><li>For Your Floors</li><li>For Your Walls</li><li>For Your Table</li><li>For Your Bedside</li><li>Let THere Be Light</li><li>Put Your Feet Up</li>
    </ul>
  </div>
  <div class="abs promo">
    <div class="promo-photo" role="img" aria-label="Kids room with white wardrobe and colourful wall shelves"></div>
    <p class="kicker">Special Offer</p>
    <p class="title">Get 20% off Now</p>
    <a class="click" href="#">Click here</a>
  </div>
</aside>

<main>
  <h2 class="abs section-title" style="left:398px;top:766px">Latest Products</h2>

  <div class="abs card" style="left:401px;top:825px"><div class="photo" role="img" aria-label="Light blue patterned throw pillow" style="background:linear-gradient(135deg,#d9ecef,#8fc4cc)"></div><p class="name">Product Name</p><p class="desc">Eget fermentum et lorem</p><div class="bar"><span class="price">$15.99</span><a class="buy" href="#">Buy Now</a></div></div>
  <div class="abs card" style="left:633px;top:825px"><div class="photo" role="img" aria-label="Wooden wall planter with red flowers" style="background:linear-gradient(180deg,#e9d9bf,#b23a2e)"></div><p class="name">Product Name</p><p class="desc">Eget fermentum et lorem</p><div class="bar"><span class="price">$15.99</span><a class="buy" href="#">Buy Now</a></div></div>
  <div class="abs card" style="left:866px;top:825px"><div class="photo" role="img" aria-label="Green plant in a concrete pot" style="background:linear-gradient(180deg,#e3f0dc,#b9bcbd)"></div><p class="name">Product Name</p><p class="desc">Eget fermentum et lorem</p><div class="bar"><span class="price">$15.99</span><a class="buy" href="#">Buy Now</a></div></div>

  <div class="abs card" style="left:401px;top:1156px"><div class="photo" role="img" aria-label="White daisies in a brown vase" style="background:linear-gradient(180deg,#f4f1e6,#6b4a3a)"></div><p class="name">Product Name</p><p class="desc">Eget fermentum et lorem</p><div class="bar"><span class="price">$15.99</span><a class="buy" href="#">Buy Now</a></div></div>
  <div class="abs card" style="left:633px;top:1156px"><div class="photo" role="img" aria-label="Orange flowers in a dark blue vase" style="background:linear-gradient(180deg,#f6c060,#1c2550)"></div><p class="name">Product Name</p><p class="desc">Eget fermentum et lorem</p><div class="bar"><span class="price">$15.99</span><a class="buy" href="#">Buy Now</a></div></div>
  <div class="abs card" style="left:866px;top:1156px"><div class="photo" role="img" aria-label="Red fringed rug" style="background:linear-gradient(180deg,#ffffff 30%,#9e1b1b 50%,#ffffff 70%)"></div><p class="name">Product Name</p><p class="desc">Eget fermentum et lorem</p><div class="bar"><span class="price">$15.99</span><a class="buy" href="#">Buy Now</a></div></div>
</main>

<section class="abs sellers" role="img" aria-label="Blurred home interior background"></section>
<h2 class="abs section-title" style="left:0;width:1200px;text-align:center;top:1572px">Top Sellings</h2>
<div class="abs card tall" style="left:130px;top:1633px"><div class="photo" role="img" aria-label="Pink checked throw pillow" style="background:linear-gradient(135deg,#e06c9a,#6a2038)"></div><p class="name">Product Name</p><p class="desc">Eget fermentum et lorem</p><div class="bar"><span class="price">$15.99</span><a class="buy" href="#">Buy Now</a></div></div>
<div class="abs card tall" style="left:374px;top:1633px"><div class="photo" role="img" aria-label="Plaid wool blanket" style="background:linear-gradient(135deg,#e3ddd2,#3a3431)"></div><p class="name">Product Name</p><p class="desc">Eget fermentum et lorem</p><div class="bar"><span class="price">$15.99</span><a class="buy" href="#">Buy Now</a></div></div>
<div class="abs card tall" style="left:618px;top:1633px"><div class="photo" role="img" aria-label="Oval woven jute rug" style="background:radial-gradient(ellipse 50% 18% at 50% 50%,#c8b08a 90%,#ffffff 100%)"></div><p class="name">Product Name</p><p class="desc">Eget fermentum et lorem</p><div class="bar"><span class="price">$15.99</span><a class="buy" href="#">Buy Now</a></div></div>
<div class="abs card tall" style="left:861px;top:1633px"><div class="photo" role="img" aria-label="Children's table and chairs in pastel colours" style="background:linear-gradient(135deg,#f6d7e0,#b8e0cf)"></div><p class="name">Product Name</p><p class="desc">Eget fermentum et lorem</p><div class="bar"><span class="price">$15.99</span><a class="buy" href="#">Buy Now</a></div></div>

<section class="abs newsletter">
  <h3>Join Our Newsletter</h3>
  <div class="field">Email address</div>
  <a class="send" href="#">Subscribe</a>
</section>

<footer>
  <div class="abs logo" style="left:127px;top:2170px;width:205px">
    <div class="word">Nestory</div>
    <div class="sub">HOME GOODS</div>
  </div>
  <div class="abs foot-col" style="left:401px;top:2170px">
    <h4>QUICK LINKS</h4>
    <ul><li>Home</li><li>About Nestory</li><li>How does this craziness work?</li><li>Contact</li></ul>
  </div>
  <div class="abs foot-col" style="left:687px;top:2170px">
    <h4>RESOURCES</h4>
    <ul><li>My Account</li><li>My Cart</li><li>Register</li><li>Sign In</li></ul>
  </div>
  <div class="abs foot-col" style="left:886px;top:2170px">
    <h4>STAY IN TOUCH</h4>
    <div class="foot-social"><span></span><span></span><span></span><span></span></div>
    <div class="pay"><span>Cardo</span><span>Amera</span><span>Orbis</span><span>Tendrix</span></div>
  </div>
  <div class="abs rule"></div>
  <p class="abs copy">© 2017 Company Name &nbsp;All right reserved</p>
</footer>

</body>
</html>
```